Clinique VeraNova business card

I am looking for a talented designer who can an existing design and make it better. I need a 2 sided business card to represent our Psychology clinic staff members. It would need to be elegant, yet modern, clean, light and uplifting. Simple design, quick turnaround time. Lots of files and logos to use as your guide. I hope to hear from you!

Target Market(s)

Clients who receive the card of our therapists

Industry/Entity Type

Health And Wellness

Contact Information for Business Card

Following the similar designs of the Maplebrook Care Center card, there will be 2 sides. Side 1 (front) should have the veranova logo instead of the maplebrook care logo, The title should read Clinique VeraNova instead of centre Bien-Être Mésange/Maplebrook care Center.

Side 2 should have a spiral similar to the one on the card with sunflower leaves, and the title of the Therapist should be Marielle Odile Brunet, Psychologue, Psychologist, her email: Marielle@Veranova-example.com and phone number should be (514) 555-0137

Font styles to use
Serif

Colors
fee18a
85cae6
ffffff
0255a3

Requirements
Must have
• Side 1 (front): veranova logo- Name of the clinic, clinic address, contact info of clinic etc. use little icons in front of each (just like on sample card)
side 2: Therapist name titles and their contact info underneath with design of spiral and/or sunflower leaves..
Nice to have
• soft colors along soft yellow/gold and blue like the logo,
mini icons for phone, email, address etc.
We do work with a holistic, zen approach so it should represent that to some extent

```html
<!DOCTYPE html>
<html lang="fr">
<head>
<meta charset="utf-8">
<title>Clinique VeraNova – Business Card</title>
<link rel="stylesheet" href="https://fonts.googleapis.com/css2?family=Tinos:wght@400;700&display=swap">
<style>
  :root {
    --stage: #dcdcdc;
    --card-white: #ffffff;
    --sun-yellow: #fae64c;
    --soft-gold: #fee18a;
    --sky-blue: #85cae6;
    --ink-navy: #1c1f5c;
    --brand-blue: #0255a3;
  }
  * { margin: 0; padding: 0; box-sizing: border-box; }
  html, body {
    width: 1200px; height: 800px; overflow: hidden;
    background: var(--stage);
    font-family: "Tinos", "Times New Roman", serif;
    color: var(--ink-navy);
  }
  .stage { position: relative; width: 1200px; height: 800px; }
  .card {
    position: absolute; top: 283px;
    width: 429px; height: 238px; overflow: hidden;
  }
  .card--front { left: 111px; background: var(--card-white); }
  .card--back { left: 638px; background: var(--sun-yellow); }

  /* Front */
  .brand-mark {
    position: absolute; left: 34px; top: 96px;
    display: flex; align-items: center; gap: 8px;
  }
  .brand-mark__dot {
    width: 26px; height: 26px; border-radius: 50%;
    background: var(--soft-gold);
  }
  .brand-mark__name {
    font-size: 31px; font-weight: 400; color: var(--ink-navy);
    letter-spacing: 0.2px;
  }
  .front-divider {
    position: absolute; left: 231px; top: 56px;
    width: 1.5px; height: 126px; background: var(--sky-blue);
  }
  .clinic-name {
    position: absolute; left: 250px; top: 55px;
    font-size: 15px; font-weight: 700;
  }
  .contact-list {
    position: absolute; left: 250px; top: 84px;
    list-style: none; font-size: 10.5px; line-height: 14px;
  }
  .contact-list li {
    display: flex; align-items: flex-start; gap: 8px;
  }
  .contact-list .gap { margin-top: 8px; }
  .contact-list .gap-sm { margin-top: 6px; }
  .icon { width: 10px; height: 11px; flex: none; margin-top: 1px; fill: var(--sky-blue); }

  /* Back */
  .swirl-field {
    position: absolute; left: 0; top: 0; width: 215px; height: 238px;
    background: radial-gradient(circle at 95px 128px,
      rgba(255,255,255,0.95) 0, rgba(255,255,255,0.55) 45px,
      rgba(255,255,255,0.25) 95px, rgba(255,255,255,0) 130px);
  }
  .therapist {
    position: absolute; left: 257px; top: 86px;
  }
  .therapist__name { font-size: 15px; font-weight: 700; line-height: 17px; }
  .therapist__title { font-size: 9.5px; line-height: 12px; }
  .therapist__contacts { list-style: none; margin-top: 6px; font-size: 10.5px; line-height: 16px; }
  .therapist__contacts li { display: flex; align-items: center; gap: 7px; }
</style>
</head>
<body>
<main class="stage">

  <section class="card card--front" aria-label="Recto">
    <div class="brand-mark">
      <span class="brand-mark__dot"></span>
      <span class="brand-mark__name">VeraNova</span>
    </div>
    <div class="front-divider"></div>
    <h1 class="clinic-name">Clinique VeraNova</h1>
    <ul class="contact-list">
      <li>
        <svg class="icon" viewBox="0 0 10 12"><path d="M5 0a4 4 0 0 0-4 4c0 3 4 8 4 8s4-5 4-8a4 4 0 0 0-4-4zm0 5.8A1.8 1.8 0 1 1 5 2.2a1.8 1.8 0 0 1 0 3.6z"/></svg>
        <span>3380 boul. des Érables ouest<br>Lachenaie, Qc., J6W 0B4</span>
      </li>
      <li class="gap">
        <svg class="icon" viewBox="0 0 10 10"><path d="M2 0.5l1.6 2.2-1 1.1a6 6 0 0 0 3.6 3.6l1.1-1L9.5 8 8.3 9.5C4 9.5 0.5 6 0.5 1.7z"/></svg>
        <span>514-555-0137</span>
      </li>
      <li class="gap">
        <svg class="icon" viewBox="0 0 10 10"><path d="M0 2h10v6H0z M0.8 2.6 5 5.6l4.2-3" fill="var(--sky-blue)" stroke="#fff" stroke-width="0.8"/></svg>
        <span>info@veranova.com</span>
      </li>
      <li>
        <svg class="icon" viewBox="0 0 10 10"><circle cx="5" cy="5" r="4.3" fill="none" stroke="var(--sky-blue)" stroke-width="1"/><ellipse cx="5" cy="5" rx="1.8" ry="4.3" fill="none" stroke="var(--sky-blue)" stroke-width="0.8"/><path d="M0.7 5h8.6" stroke="var(--sky-blue)" stroke-width="0.8"/></svg>
        <span>www.veranova.com</span>
      </li>
      <li>
        <svg class="icon" viewBox="0 0 10 10"><circle cx="5" cy="5" r="4.5"/></svg>
        <span>www.social-example.com/VeraNova</span>
      </li>
    </ul>
  </section>

  <section class="card card--back" aria-label="Verso">
    <div class="swirl-field" role="img" aria-label="Large white spiral decoration on yellow"></div>
    <div class="therapist">
      <h2 class="therapist__name">Marielle Odile Brunet</h2>
      <p class="therapist__title">Psychologue, Psychologist,</p>
      <ul class="therapist__contacts">
        <li>
          <svg class="icon" viewBox="0 0 8 11"><rect x="0.6" y="0.6" width="6.8" height="9.8" rx="1.2" fill="none" stroke="var(--sky-blue)" stroke-width="1.1"/><circle cx="4" cy="8.6" r="0.7"/></svg>
          <span>(514) 555-0137</span>
        </li>
        <li>
          <svg class="icon" viewBox="0 0 10 10"><path d="M0 2h10v6H0z M0.8 2.6 5 5.6l4.2-3" fill="var(--sky-blue)" stroke="var(--sun-yellow)" stroke-width="0.8"/></svg>
          <span>Marielle@Veranova-example.com</span>
        </li>
      </ul>
    </div>
  </section>

</main>
</body>
</html>
```